Business Card Design for Online Gift Business

Business card design for a new online Canadian company called "Harlow & Reed Gift Crates" selling modern and luxurious gift boxes for every occasion. Items are sourced locally from talented socially-responsible Canadian artisans. Each gift is elegantly presented in a keepsake wood box to ensure a lasting impression.

Industry/Entity Type

E-Commerce

Contact Information for Business Card

Merin Holloway, Proprietor
Calgary, AB
587-214-3306
www.harlowandreed.ca
hello@harlowandreed.ca

Requirements
Must have
• Gifts from our best, to your best
• Please also include the symbols for Facebook and Instagram
Nice to have
• **I have attached a few samples of background colors and font colors that I like. I hope this helps in a few directions to try.

```html
<!DOCTYPE html>
<html lang="en">
<head>
<meta charset="utf-8">
<title>Harlow &amp; Reed Gift Crates – Business Card</title>
<link rel="stylesheet" href="https://fonts.googleapis.com/css2?family=Arimo:wght@400;700&display=swap">
<style>
  :root {
    --backdrop: #2a2522;
    --card-black: #121212;
    --card-edge: #1d1d1d;
    --gold: #a89272;
    --gold-bright: #c5a56d;
    --text-light: #e6e6e6;
    --text-muted: #bdbdbd;
    --divider: #8c8c8c;
  }
  * { box-sizing: border-box; margin: 0; padding: 0; }
  html, body {
    width: 1200px;
    height: 864px;
    overflow: hidden;
    background: var(--backdrop);
    font-family: "Arimo", Arial, sans-serif;
  }
  .sheet {
    width: 1200px;
    height: 864px;
    display: flex;
    flex-direction: column;
    align-items: center;
    justify-content: center;
    gap: 28px;
  }
  .card {
    width: 700px;
    height: 400px;
    background: var(--card-black);
    border: 1px solid var(--card-edge);
    box-shadow: 0 10px 30px rgba(0,0,0,0.45);
    position: relative;
  }

  /* Front */
  .card-front {
    display: flex;
    flex-direction: column;
    align-items: center;
    justify-content: center;
  }
  .brand-name {
    color: var(--gold);
    font-weight: 400;
    letter-spacing: 0.04em;
    white-space: nowrap;
  }
  .card-front .brand-name { font-size: 54px; }
  .tagline {
    color: var(--text-muted);
    font-size: 15px;
    font-style: normal;
    letter-spacing: 0.06em;
    margin-top: 14px;
  }
  .card-front .web-address {
    color: var(--text-muted);
    font-size: 15px;
    letter-spacing: 0.32em;
    margin-top: 34px;
  }

  /* Back */
  .card-back {
    display: flex;
    align-items: center;
    padding: 0 40px 0 46px;
  }
  .card-back .brand-name {
    font-size: 36px;
    width: 300px;
    text-align: center;
  }
  .divider {
    width: 1px;
    height: 250px;
    background: linear-gradient(to bottom, transparent, var(--divider) 20%, var(--divider) 80%, transparent);
    margin: 0 32px 0 22px;
  }
  .contact { display: flex; flex-direction: column; }
  .contact-name {
    color: var(--gold-bright);
    font-weight: 700;
    font-size: 24px;
    letter-spacing: 0.02em;
  }
  .contact-title {
    color: var(--text-light);
    font-size: 17px;
    margin-top: 4px;
  }
  .contact-city {
    color: var(--text-muted);
    font-size: 15px;
    margin-top: 18px;
  }
  .contact-line {
    display: flex;
    align-items: center;
    gap: 10px;
    color: var(--text-light);
    font-size: 16px;
    margin-top: 10px;
    white-space: nowrap;
  }
  .contact-icon { width: 16px; height: 16px; flex: none; }
  .social-row {
    display: flex;
    align-items: center;
    gap: 8px;
    color: var(--text-muted);
    font-size: 15px;
    margin-top: 16px;
  }
  .social-dot {
    width: 16px;
    height: 16px;
    border-radius: 50%;
    background: var(--gold-bright);
    flex: none;
  }
  .social-handle { margin-left: 2px; }
</style>
</head>
<body>
  <main class="sheet">
    <section class="card card-front" aria-label="Business card front">
      <div class="brand-name">Harlow &amp; Reed</div>
      <div class="tagline">Gifts from our best, to your best</div>
      <div class="web-address">www.harlowandreed.ca</div>
    </section>

    <section class="card card-back" aria-label="Business card back">
      <div class="brand-name">Harlow &amp; Reed</div>
      <div class="divider"></div>
      <div class="contact">
        <div class="contact-name">Merin Holloway</div>
        <div class="contact-title">Proprietor</div>
        <div class="contact-city">Calgary, AB</div>
        <div class="contact-line">
          <svg class="contact-icon" viewBox="0 0 16 16" aria-hidden="true">
            <circle cx="8" cy="8" r="8" fill="var(--gold-bright)"/>
            <path d="M5.2 3.8l1.3 1.5-.8 1.1c.5 1.2 1.5 2.2 2.7 2.7l1.1-.8 1.5 1.3-.6 1.5c-3.1-.3-5.8-3-6.1-6.1z" fill="var(--card-black)"/>
          </svg>
          <span>587-214-3306</span>
        </div>
        <div class="contact-line">
          <svg class="contact-icon" viewBox="0 0 16 16" aria-hidden="true">
            <circle cx="8" cy="8" r="8" fill="var(--gold-bright)"/>
            <circle cx="8" cy="8" r="4.5" fill="none" stroke="var(--card-black)" stroke-width="1.1"/>
            <ellipse cx="8" cy="8" rx="2" ry="4.5" fill="none" stroke="var(--card-black)" stroke-width="1.1"/>
            <line x1="3.5" y1="8" x2="12.5" y2="8" stroke="var(--card-black)" stroke-width="1.1"/>
          </svg>
          <span>www.harlowandreed.ca</span>
        </div>
        <div class="contact-line">
          <svg class="contact-icon" viewBox="0 0 16 16" aria-hidden="true">
            <circle cx="8" cy="8" r="8" fill="var(--gold-bright)"/>
            <rect x="4" y="5.2" width="8" height="5.6" fill="none" stroke="var(--card-black)" stroke-width="1.1"/>
            <path d="M4 5.4l4 3 4-3" fill="none" stroke="var(--card-black)" stroke-width="1.1"/>
          </svg>
          <span>hello@harlowandreed.ca</span>
        </div>
        <div class="social-row">
          <span class="social-dot" role="img" aria-label="Social profile symbol"></span>
          <span class="social-dot" role="img" aria-label="Social profile symbol"></span>
          <span class="social-handle">@harlowandreed</span>
        </div>
      </div>
    </section>
  </main>
</body>
</html>
```